Case Pack Design for a new Veggie Chip Brand

Looking for an eye-catching design to cover our case pack boxes for a new Veggie Chip brand made with sustainable (upcycled) ingredients. Our case packs will create “case stacks” on the grocery store floor, which means product will be displayed in the case with a tear-off front of the box. For example, 4 cases might be stacked to make a column of product during promotions, in the produce department of the grocery store.
We’re a brand with a lot to say - and we want our case boxes to be an eye-catching, bold design that makes people stop to grab the product and see what we’re all about.
The case pack design will be descriptive with slogans that tell people more about the product, brand and mission.
Updates

Target Market(s)

Health + sustainability-oriented snack consumers

Industry/Entity Type

Food & Beverage

Font styles to use
Serif
Other font styles liked:
• Retro Fonts encouraged! Bold & Wavy fonts also welcome with a mix of newstext for smaller text details

Colors

Designer to choose only greyscale colors for use in the design.

Requirements
Must have
• Will need to meet design guidelines as outlined in presentation deck, and dielines to follow
Nice to have
• I am leaning towards moodboard 1 (maybe can be combined with some elements of 2) and 3 -- see the design deck attached
Should not have
• Only 1 color print - use black as a default to start, but we might do an orange or green

```html
<!DOCTYPE html>
<html lang="en">
<head>
<meta charset="utf-8">
<title>Peel Provisions – Case Pack</title>
<link href="https://fonts.googleapis.com/css2?family=Courier+Prime:wght@700&family=Alfa+Slab+One&display=swap" rel="stylesheet">
<style>
  :root {
    --paper: #ffffff;
    --field: #5c5c5c;
    --block: #3d3d3d;
    --banner: #8c8c8c;
    --light-field: #a9a9a9;
    --card: #e6e6e6;
    --tag: #262626;
    --sub-banner: #b3b3b3;
    --sun: #9a9a9a;
    --ink: #0b0b0b;
    --ring: #d4d4d4;
    --tag-text: #f2f2f2;
  }
  html, body {
    margin: 0;
    padding: 0;
    width: 1200px;
    height: 853px;
    overflow: hidden;
    background: var(--paper);
  }
  .case-panel {
    display: block;
    width: 1200px;
    height: 853px;
  }
  .slab-type {
    font-family: "Courier Prime", "Courier New", monospace;
    font-weight: 700;
  }
  .tag-type {
    font-family: "Alfa Slab One", Georgia, serif;
  }
</style>
</head>
<body>
<svg class="case-panel" viewBox="0 0 1407 1000" xmlns="http://www.w3.org/2000/svg">
  <rect class="paper" width="1407" height="1000" fill="var(--paper)"/>
  <polygon class="main-field" points="0,170 150,0 1407,0 1407,975 1300,1000 0,1000" fill="var(--field)"/>

  <polygon class="light-field-top" points="640,90 700,0 1407,0 1407,420 1300,400 1000,260" fill="var(--light-field)"/>
  <polygon class="light-field-leaf" points="150,360 560,280 650,420 740,700 620,770 330,930 300,700 240,580" fill="var(--light-field)"/>

  <polygon class="dark-block" points="30,250 175,0 680,0 460,450" fill="var(--block)" stroke="var(--ink)" stroke-width="2"/>

  <g class="pattern-card" role="img" aria-label="Retro print of striped and speckled half circles on a pale card">
    <polygon points="700,115 905,0 1380,430 1110,690" fill="var(--card)"/>
  </g>

  <polygon class="headline-banner" points="180,140 225,0 1030,240 975,400" fill="var(--banner)" stroke="var(--ink)" stroke-width="4"/>
  <text class="slab-type headline" x="245" y="95" font-size="60" fill="var(--ink)" transform="rotate(17 245 95)">SNACK WITH IMPACT</text>

  <circle class="brand-ring" cx="375" cy="445" r="290" fill="none" stroke="var(--ring)" stroke-width="1.2"/>

  <text class="slab-type brand-name" x="235" y="375" font-size="130" fill="var(--paper)" textLength="320" lengthAdjust="spacingAndGlyphs">PEEL</text>
  <text class="slab-type brand-name" x="145" y="525" font-size="76" fill="var(--paper)" textLength="460" lengthAdjust="spacingAndGlyphs">PROVISIONS</text>

  <text class="tag-type tagline-lead" x="400" y="585" font-size="30" fill="var(--tag)" transform="rotate(-17 400 585)">IT'S</text>
  <g class="crunch-tag" transform="translate(440,712) rotate(-17)">
    <rect x="0" y="-100" width="620" height="110" fill="var(--tag)"/>
    <text class="tag-type" x="330" y="-20" font-size="80" text-anchor="middle" fill="var(--tag-text)">CRUNCH</text>
  </g>
  <g class="time-tag" transform="translate(785,700) rotate(-17)">
    <rect x="0" y="-95" width="420" height="100" fill="var(--tag)"/>
    <text class="tag-type" x="225" y="-18" font-size="76" text-anchor="middle" fill="var(--tag-text)">TIME</text>
  </g>
  <text class="slab-type tagline-end" x="1215" y="580" font-size="82" fill="var(--ink)" transform="rotate(-45 1215 580)">LIFE</text>

  <g class="sub-banner" transform="translate(85,850) rotate(-8.5)">
    <rect x="0" y="-10" width="745" height="82" fill="var(--sub-banner)" stroke="var(--ink)" stroke-width="5"/>
    <text class="slab-type" x="372" y="45" font-size="31" text-anchor="middle" fill="var(--ink)">NOT YOUR AVERAGE VEGGIE CHIP</text>
  </g>

  <g class="growth-art" role="img" aria-label="Illustration of seedlings sprouting under falling rain in front of a round sun">
    <ellipse cx="1070" cy="830" rx="180" ry="135" fill="var(--sun)" stroke="var(--ink)" stroke-width="4"/>
  </g>
</svg>
</body>
</html>
```